Pimbrox

Squarespace website for specialty health based ingredients, like organic Galactose, CBD Oil, Hyaluronic Acid. Already have a logo that I want to use.
Updates

Reason: Too few designs submitted. I would like to see what other designers can do.

I am not sure that I am getting what I need. I was hoping for a fully working Squarespace Website and listed that as uncoded. But, I think that it has to be fully coded and then I import it to my SquareSpace to get the functional website and request that Orvanix hosts the site. I mentioned that I want my office to be able to make revisions, etc but they will not know HTML nor be able convert it themselves. May I get an explanation? I do see several designs that I really like. But, am unclear exactly what I am purchasing and will eventually own.

Target Market(s)

Buyers of bulk chemicals used in the manufacture of pharmaceuticals, supplements, specialty foods and beverages.

Industry/Entity Type

Health And Wellness

Number of Pages Required

5+ page

Font styles to use
Sans Serif

Colors
33b8a4
add136
34a7d8

Requirements
Must have
• Please see Quillmere Fathom, Inc website for the pages that I need. I want a similar set up for products, only for specialty usually plant-based chemicals. Mapping should be the same.
Nice to have
• Brief content on a sample product such as pure CBD Oil or Galactose (D+) as examples. I would like a SquareSpace design if possible so that my staff can make changes readily. Would like to have Orvanix host the site once completed. Not sure what is Uncoded web design vs.Coded. Please help me know how to answer that question.
Should not have
• Please no association with Marijuana. This CBD Hemp Oil is 99.9% free of THC and imported into the United States legally. No people, needles, social networking, or newsletter necessary. Most of the designs are very tiny logos, could be bigger.

```html
<!DOCTYPE html>
<html lang="en">
<head>
<meta charset="utf-8">
<title>Pimbrox Inc. — Health Based Ingredients</title>
<link rel="stylesheet" href="https://fonts.googleapis.com/css2?family=Mulish:wght@400;600;700&family=Open+Sans:wght@400;600&display=swap">
<style>
  :root {
    --teal: #33b8a4;
    --green: #6e9c1c;
    --ink: #1e1e1e;
    --muted: #8a8a8a;
    --body: #555555;
    --white: #ffffff;
    --forest-top: #2f4a22;
    --forest-mid: #5f8a3a;
    --forest-low: #3a4a2c;
    --coral-a: #ef3b3f;
    --coral-b: #f4868a;
    --herb-a: #4f7a2e;
    --herb-b: #9c6a2c;
    --skin-a: #9a9593;
    --skin-b: #cbbcb4;
    --card-line: #e4e4e4;
  }
  * { margin: 0; padding: 0; box-sizing: border-box; }
  html, body { width: 1200px; height: 3082px; overflow: hidden; background: var(--white); }
  body { position: relative; font-family: "Mulish", sans-serif; color: var(--ink); }
  .abs { position: absolute; }
  .center { left: 0; width: 1200px; text-align: center; }

  /* Hero */
  .hero { top: 0; left: 0; width: 1200px; height: 571px;
    background: radial-gradient(ellipse at 50% 35%, var(--forest-mid) 0%, var(--forest-top) 55%, var(--forest-low) 100%); }
  .brand { top: 30px; left: 108px; display: flex; align-items: center; gap: 16px; color: var(--white); }
  .brand-mark { width: 68px; height: 68px; border-radius: 50%; background: var(--white); }
  .brand-name { font-size: 50px; font-weight: 700; letter-spacing: .5px; line-height: 1; }
  .nav { top: 52px; left: 522px; display: flex; }
  .nav a { color: var(--white); text-decoration: none; font-size: 17px; font-weight: 600; letter-spacing: .5px;
    height: 42px; line-height: 40px; padding: 0 20px; margin-right: 10px; border: 1px solid transparent; }
  .nav a.active { border-color: rgba(255,255,255,.85); }
  .hero-title { top: 244px; font-size: 42px; font-weight: 400; color: var(--white); letter-spacing: 1px; }
  .hero-sub { top: 300px; font-size: 27px; font-weight: 400; color: var(--white); letter-spacing: 1px; }
  .hero-btn { top: 358px; left: 530px; width: 138px; height: 39px; background: var(--teal); color: var(--white);
    font-size: 17px; line-height: 39px; text-align: center; }
  .dots { top: 528px; left: 552px; display: flex; gap: 8px; }
  .dots span { width: 14px; height: 14px; border-radius: 50%; background: var(--white); }
  .dots span.ring { background: transparent; border: 2px solid var(--white); }

  /* Welcome */
  .section-title { font-size: 37px; font-weight: 400; color: var(--ink); }
  .welcome-title { top: 608px; }
  .lead { top: 660px; left: 140px; width: 920px; text-align: center; font-size: 18px; line-height: 28px; color: var(--muted); }

  .product { top: 777px; width: 310px; text-align: center; }
  .product-img { height: 216px; border: 1px solid var(--card-line); }
  .img-plant { background: linear-gradient(180deg, #fafafa, #e8efe2); }
  .img-oil { background: linear-gradient(160deg, #f6f1e2, #b79a45 70%, #6d8a33); }
  .img-vial { background: linear-gradient(180deg, #8a9298, #c7ccce 60%, #9fa7ab); }
  .product h3 { margin-top: 12px; font-size: 23px; font-weight: 700; color: var(--green); }
  .small { font-family: "Open Sans", sans-serif; font-size: 13.5px; line-height: 23px; color: var(--body); }
  .product .small { font-size: 12.2px; }
  .product p { margin-top: 8px; padding: 0 6px; }

  /* Bands */
  .band { left: 0; width: 1200px; display: flex; align-items: center; justify-content: center; }
  .band span { font-size: 38px; color: var(--white); letter-spacing: 1px; }
  .band-why { top: 1262px; height: 273px; background: linear-gradient(90deg, var(--coral-a), var(--coral-b) 50%, var(--coral-a)); }
  .band-blog { top: 1810px; height: 282px; background: linear-gradient(90deg, var(--herb-a), #6c8a3a 45%, var(--herb-b) 75%, #8a6b4a); }
  .band-test { top: 2398px; height: 270px; background: linear-gradient(90deg, var(--skin-a), var(--skin-b) 55%, #8f8c86); }

  .sub-title { font-size: 23px; font-weight: 600; color: var(--green); }
  .benefits-title { top: 1594px; }
  .benefits-text { top: 1630px; left: 270px; width: 660px; text-align: center; }

  .col { width: 360px; text-align: center; }
  .col p { margin-top: 6px; }
  .blog-1 { top: 2164px; left: 229px; }
  .blog-2 { top: 2164px; left: 630px; }
  .test-1 { top: 2744px; left: 229px; }
  .test-2 { top: 2744px; left: 630px; }

  /* Footer */
  .footer { top: 2947px; left: 0; width: 1200px; height: 135px; background: var(--teal); color: var(--white);
    display: flex; align-items: center; justify-content: center; }
  .footer p { font-family: "Open Sans", sans-serif; font-size: 13.5px; }
</style>
</head>
<body>

  <header class="abs hero" role="img" aria-label="Photo looking up into a green forest canopy"></header>
  <div class="abs brand"><span class="brand-mark"></span><span class="brand-name">Pimbrox</span></div>
  <nav class="abs nav">
    <a class="active" href="#">HOME</a><a href="#">PRODUCT</a><a href="#">ABOUT</a><a href="#">WHY US</a><a href="#">CONTACT</a>
  </nav>
  <h1 class="abs center hero-title">We make Health based Ingredients</h1>
  <p class="abs center hero-sub">Morbi porta libero ullamcorper nonummy</p>
  <a class="abs hero-btn">Read More</a>
  <div class="abs dots"><span class="ring"></span><span></span><span></span><span></span></div>

  <h2 class="abs center section-title welcome-title">Welcome to Pimbrox Inc.</h2>
  <p class="abs lead">commodo a mi Morbi ornare gravida elit Integer congue augue et malesuada iaculis ipsum dui aliquet felis at cursus magna nisl nec elit Praesent elementum elit at tellus nec ultricies</p>

  <article class="abs product" style="left:111px">
    <div class="product-img img-plant" role="img" aria-label="Potted green seedling"></div>
    <h3>Organic Galactose</h3>
    <p class="small">commodo a mi Morbi ornare gravida elit Integer congue augue et malesuada iaculis ipsum dui aliquet felis at cursus magna nisl nec elit Praesent elementum elit at tellus nec ultricies sit amet porttitor mattis enim In massa lib</p>
  </article>
  <article class="abs product" style="left:445px">
    <div class="product-img img-oil" role="img" aria-label="Jar of oil with seeds on a wooden scoop and leaves"></div>
    <h3>CBD Oil</h3>
    <p class="small">commodo a mi Morbi ornare gravida elit Integer congue augue et malesuada iaculis ipsum dui aliquet felis at cursus magna nisl nec elit Praesent elementum elit at tellus nec ultricies sit amet porttitor mattis enim In massa lib</p>
  </article>
  <article class="abs product" style="left:779px">
    <div class="product-img img-vial" role="img" aria-label="Row of glass ampoules"></div>
    <h3>Hyaluronic Acid</h3>
    <p class="small">commodo a mi Morbi ornare gravida elit Integer congue augue et malesuada iaculis ipsum dui aliquet felis at cursus magna nisl nec elit Praesent elementum elit at tellus nec ultricies sit amet porttitor mattis enim In massa lib</p>
  </article>

  <section class="abs band band-why" role="img" aria-label="Soft red-toned skincare photo"><span>Why Choose Us</span></section>
  <h3 class="abs center sub-title benefits-title">Benefits of our products</h3>
  <p class="abs small benefits-text">aptain &amp; Maritime eleifend libero a tempus libero lectus feugiat felis Morbi diam mauris viverra in gravida eu mattis in ante Morbi eget arcu Morbi porta libero id ullamcorper nonummy nibh ligula pulvinar metus eget consectetuer augue nisi quis lacus Ut ac mi quis lacus mollis aliquam Curabitur</p>

  <section class="abs band band-blog" role="img" aria-label="Fresh herb leaves beside amber oil bottles"><span>From Our Blogs</span></section>
  <article class="abs col blog-1">
    <h3 class="sub-title">Blog Tittle here</h3>
    <p class="small">aptain &amp; Maritime eleifend libero a tempus libero lectus feugiat felis Morbi diam mauris viverra in gravida eu mattis in ante Morbi eget arcu Morbi porta libero</p>
  </article>
  <article class="abs col blog-2">
    <h3 class="sub-title">Blog Tittle here</h3>
    <p class="small">aptain &amp; Maritime eleifend libero a tempus libero lectus feugiat felis Morbi diam mauris viverra in gravida eu mattis in ante Morbi eget arcu Morbi porta libero</p>
  </article>

  <section class="abs band band-test" role="img" aria-label="Soft muted skincare photo"><span>Testimonials</span></section>
  <article class="abs col test-1">
    <h3 class="sub-title">Ante enim dapibu</h3>
    <p class="small">aptain &amp; Maritime eleifend libero a tempus libero lectus feugiat felis Morbi diam mauris viverra in gravida eu mattis in ante Morbi eget arcu Morbi porta libero</p>
  </article>
  <article class="abs col test-2">
    <h3 class="sub-title">Curabitur tristique</h3>
    <p class="small">aptain &amp; Maritime eleifend libero a tempus libero lectus feugiat felis Morbi diam mauris viverra in gravida eu mattis in ante Morbi eget arcu Morbi porta libero</p>
  </article>

  <footer class="abs footer">
    <p>© 2016 Company Name &nbsp;All right reserved &nbsp;Term of Use</p>
  </footer>

</body>
</html>
```